Homepage mockup for PivotMarkScore.com

I would like a homepage mockup of pivotmarkscore.com.

Basically what the site does, is it allows a person to upload a video of a gymnastics routine and our certified judges will judge the routine providing a score, as well as provide a critique and feedback as to why they gave you that score. Many times people don't know why they got the score they did at a gymnastics competition, so this site aims to provide reasoning behind it.

I have started to design the homepage myself (see attached), and like it, but I'd like a professional to finish the layout, or even come up with something really wow and original. I like clean, typically simple design.

THIS IS AN OLD VERSION OF THE SITE (http://esite.krelnavo.com/) This should only be used so you can get an idea of what the site is about. I DO NOT want the new site to look like this, but the basic concept and content remains the same.

DESIGNER FILES CAN BE DOWNLOADED HERE (http://krelnavo.com/files.aspx)

Target Market(s)

Gymnastic type people, parents of gymnasts, coaches, etc.

Industry/Entity Type

It Professional

Requirements
Must have
• -The pivot mark logo (provided)
-Not required, but I have attached the main photo I used in my mockup (AI File)
*A step by step graphic(s) depicting the process for a user. A How it works sort of explanation. Should be eye catching, not just text.

-Step 1: Videotape your gymnastic routine.
-Step 2: Create an account and share us your video.
-Step 3: Our certified judges will score and critique your routine, fully explaining the reasons behind their score.

```html
<!DOCTYPE html>
<html lang="en">
<head>
<meta charset="utf-8">
<title>PivotMarkScore.com – Home</title>
<link href="https://fonts.googleapis.com/css2?family=Ubuntu:ital,wght@0,400;0,500;0,700;1,400&family=Open+Sans:ital,wght@0,400;1,400&display=swap" rel="stylesheet">
<style>
  :root{
    --blue-dark:#1a3a9c;
    --blue:#2a52c4;
    --blue-mid:#3c6bd6;
    --steel:#4a76b0;
    --navy-text:#1d4f9a;
    --orange:#f39a12;
    --orange-dark:#e0840a;
    --grey-text:#666;
    --light-grey:#9a9a9a;
    --rule:#e4e4e4;
    --white:#fff;
  }
  *{box-sizing:border-box;margin:0;padding:0}
  html,body{width:1200px;height:1164px;overflow:hidden;background:var(--white)}
  body{position:relative;font-family:'Ubuntu',sans-serif}
  .abs{position:absolute}

  /* header */
  .site-header{left:0;top:0;width:1200px;height:116px;background:linear-gradient(#1d3fa8,#2b55c6 60%,#2248b5);border-bottom:1px solid #173a96}
  .brand{left:147px;top:38px;display:flex;align-items:center;gap:10px;color:var(--white);font-size:30px;font-weight:500;letter-spacing:-.5px}
  .brand-mark{width:26px;height:26px;background:var(--orange);border-radius:4px}
  .member-login{left:920px;top:0;width:128px;height:31px;background:linear-gradient(#e4e4e4,#c9c9c9);border-radius:0 0 12px 12px;color:#666;font:italic 14px 'Open Sans',sans-serif;text-align:center;line-height:30px}
  .main-nav{left:455px;top:65px;display:flex;align-items:center;height:39px}
  .main-nav a{color:var(--white);text-decoration:none;font-size:18px;margin-right:47px}
  .main-nav a.active{background:linear-gradient(#f7ac2d,var(--orange-dark));border-radius:20px;padding:0 23px;line-height:39px;margin-right:28px}

  /* hero */
  .hero{left:0;top:116px;width:1200px;height:609px;
    background:linear-gradient(180deg,#f1f0ee 0%,#f5f4f2 70%,#e6d7c4 80%,#d8c2a6 88%,#7a7a7a 90%,#bdbdbd 96%,#fff 100%)}
  .hero-figure{left:570px;top:160px;width:470px;height:480px;border-radius:40% 30% 20% 40%;background:radial-gradient(#3a3a3a 0%,#777 45%,rgba(240,240,240,0) 72%);opacity:.55}
  .video-frame{left:212px;top:165px;width:354px;height:250px;background:#e2e2e2;transform:rotate(-3.5deg);padding:10px;box-shadow:0 2px 6px rgba(0,0,0,.15)}
  .video-still{width:100%;height:100%;background:linear-gradient(#a9b0b2,#94999c)}
  .play-btn{left:354px;top:251px;width:66px;height:66px;border-radius:50%;background:#000}
  .play-btn::after{content:"";position:absolute;left:27px;top:21px;border-left:16px solid #fff;border-top:12px solid transparent;border-bottom:12px solid transparent}
  .tagline{left:187px;top:444px;font-size:29px;color:#5d5d5d}
  .tagline-accent{left:207px;top:482px;font-size:30px;font-weight:500;color:var(--steel)}
  .cta{left:258px;top:530px;width:258px;height:58px;border-radius:14px;background:#9e9e9e;padding:5px}
  .cta-inner{height:100%;border-radius:10px;background:linear-gradient(#3f6ee0,#1e44b2);display:flex;align-items:center;padding-left:12px;color:var(--white);gap:14px}
  .cta-small{font-size:12px;line-height:12px;font-weight:500}
  .cta-big{font-size:21px;font-weight:700;letter-spacing:-.3px}

  /* steps */
  .step-num{width:84px;height:84px;border-radius:50%;color:var(--white);font-size:40px;text-align:center;line-height:84px}
  .step-num.orange{background:linear-gradient(#f7ac2d,var(--orange-dark))}
  .step-num.blue{background:var(--steel)}
  .step-text{font-size:18px;line-height:21.5px}
  .divider{left:100px;top:866px;width:1000px;height:1px;background:var(--rule)}

  /* lower */
  .section-title{font-size:18px;color:var(--orange-dark)}
  .news-date{font:italic 11px 'Open Sans',sans-serif;color:var(--orange-dark);font-weight:600}
  .small-copy{font:italic 11px/14px 'Open Sans',sans-serif;color:#555}
  .col-rule{left:599px;top:888px;width:1px;height:158px;background:var(--rule)}
  .mail-icon{left:652px;top:938px}
  .mail-input{left:708px;top:950px;width:290px;height:40px;border-radius:20px;background:linear-gradient(#f4f4f4,#fff);box-shadow:inset 0 2px 3px rgba(0,0,0,.08)}
  .go-btn{left:957px;top:947px;width:49px;height:46px;border-radius:23px;background:linear-gradient(#f7ac2d,var(--orange-dark));color:var(--white);font-size:22px;text-align:center;line-height:46px}

  /* footer */
  .site-footer{left:0;top:1074px;width:1200px;height:48px;background:linear-gradient(#2a52c4,#1e42ad)}
  .footer-nav{left:114px;top:1090px;display:flex;gap:0}
  .footer-nav a{color:var(--white);text-decoration:none;font-size:14px;margin-right:36px}
  .social{left:824px;top:1082px;display:flex;gap:8px}
  .social span{width:32px;height:32px;border-radius:50%;background:#5b7fb8;border:1px solid rgba(255,255,255,.4)}
  .copyright{left:0;top:1137px;width:1200px;text-align:center;font:italic 11px 'Open Sans',sans-serif;color:#666}
</style>
</head>
<body>

<header class="abs site-header"></header>
<div class="abs brand"><span class="brand-mark"></span>The pivot mark</div>
<div class="abs member-login">Member Login</div>
<nav class="abs main-nav">
  <a class="active" href="#">Home</a><a href="#">About</a><a href="#">Services</a><a href="#">FAQ</a><a href="#">News</a><a href="#">Contact Us</a>
</nav>

<section class="abs hero" role="img" aria-label="Photo of a gymnast doing a split handstand on a balance beam"></section>
<div class="abs hero-figure" aria-hidden="true"></div>
<div class="abs video-frame"><div class="video-still" role="img" aria-label="Video still of a gymnast leaping"></div></div>
<div class="abs play-btn" aria-label="Play video"></div>
<p class="abs tagline">Judges only give you a number...</p>
<p class="abs tagline-accent">... We explain the reason</p>
<a class="abs cta" href="#"><span class="cta-inner"><span class="cta-small">Upload your video<br>&nbsp;&nbsp;&amp; get critiqued!</span><span class="cta-big">Get started</span></span></a>

<div class="abs step-num orange" style="left:114px;top:738px">01</div>
<p class="abs step-text" style="left:213px;top:767px;color:var(--light-grey)">Videotape your<br>gymnastic routine.</p>
<div class="abs step-num blue" style="left:428px;top:738px">02</div>
<p class="abs step-text" style="left:518px;top:767px;color:var(--navy-text)">Create an account and<br>share us your video.</p>
<div class="abs step-num blue" style="left:741px;top:738px">03</div>
<p class="abs step-text" style="left:832px;top:757px;color:var(--navy-text)">Our certified judges will score<br>and critique your routine,<br>fully explaining the reasons<br>behind their score</p>
<div class="abs divider"></div>

<h2 class="abs section-title" style="left:151px;top:892px;font-weight:400">News Feed</h2>
<p class="abs news-date" style="left:151px;top:931px">01 - jan -12</p>
<p class="abs small-copy" style="left:151px;top:950px">Sed ut perspiciatis unde omnis iste natus error sit voluptatem accusantium<br>doloremque laudantium, totam rem aperiam, eaque ipsa quae ab illo inventore</p>
<p class="abs news-date" style="left:151px;top:992px">01 - jan -12</p>
<p class="abs small-copy" style="left:151px;top:1011px">Sed ut perspiciatis unde omnis iste natus error sit voluptatem accusantium<br>doloremque laudantium, totam rem aperiam, eaque ipsa quae ab illo inventore</p>
<div class="abs col-rule"></div>

<h2 class="abs section-title" style="left:650px;top:892px;font-weight:400">Join our mailing List</h2>
<svg class="abs mail-icon" width="50" height="50" viewBox="0 0 50 50" aria-hidden="true">
  <path d="M2 20 L25 2 L48 20 V48 H2 Z" fill="#d9d9d9"/>
  <rect x="9" y="8" width="32" height="26" fill="#f5a623"/>
  <text x="25" y="27" font-size="16" text-anchor="middle" fill="#fff" font-family="Ubuntu,sans-serif">@</text>
  <path d="M2 20 L25 36 L48 20 V48 H2 Z" fill="#e8e8e8" stroke="#c4c4c4"/>
</svg>
<div class="abs mail-input"></div>
<div class="abs go-btn">GO</div>
<p class="abs small-copy" style="left:653px;top:1012px">Sed ut perspiciatis unde omnis iste natus error sit voluptatem<br>accusantium doloremque laudantium, totam rem aperiam, eaque<br>ipsa quae ab illo inventore</p>

<footer class="abs site-footer"></footer>
<nav class="abs footer-nav">
  <a href="#">Home</a><a href="#">About</a><a href="#">Services</a><a href="#">FAQ</a><a href="#">News</a><a href="#">Contact Us</a>
</nav>
<div class="abs social" aria-label="Social links"><span></span><span></span><span></span><span></span><span></span></div>
<p class="abs copyright">© 2012.www.pivotmarkscore.com</p>

</body>
</html>
```